Wix Web design for a Residential redevelopment company

I need a website with a modern and elegant feel that will attract investors. I would like for the color scale to include the colors in our logo and also shades of grey for a modern feel. I need a page for property case studies in which each case study includes property before and after photos, an imbeded youtube video and text in the format of a math problem showing the amount the property was bought for -(minus) what the investor got in return -(minus) rehab costs -(minus) taxes and fees =(equals) Net Profit
However instead of there being an equal sign, I want the math problem to go vertically down with an underline for the equals sign.There needs to be an "About us," page, Investor Inquiries page, Contact Us Page, and Case studies page.
For font formatting, we like Corporate Gothic. Please make the website Wix friendly.

When someone clicks on one of the case study pictures, I would like the pictures to pull up in a click or swipe to the right manner similar to how pictures are structured on mebrank or pendosa.com

Target Market(s)

Investors

Industry/Entity Type

Real Estate

Number of Pages Required

5+ page

Font styles to use
Other font styles liked:
• Gothic Corporate

Requirements
Nice to have
• stock photos for the home page

```html
<!DOCTYPE html>
<html lang="en">
<head>
<meta charset="utf-8">
<title>Velmora Property Solutions – Case Study</title>
<link href="https://fonts.googleapis.com/css2?family=Montserrat:wght@400;500;600;700&family=Open+Sans:wght@400;600;700&display=swap" rel="stylesheet">
<style>
:root{
  --green:#3aa335;
  --green-dark:#2a8a27;
  --blue:#1a6fc9;
  --blue-dark:#0f56a8;
  --ink:#222;
  --text:#444;
  --muted:#777;
  --line:#dcdcdc;
  --pale:#f5f5f5;
  --band:#e9ebe8;
  --black:#0b0b0b;
  --icon:#9a9a9a;
}
*{margin:0;padding:0;box-sizing:border-box}
html,body{width:1200px;height:2503px;overflow:hidden;background:#fff}
body{position:relative;font-family:"Open Sans",Arial,sans-serif;color:var(--text);font-size:12px}
.abs{position:absolute}
/* hero */
.hero-before{left:0;top:0;width:594px;height:400px;background:linear-gradient(180deg,#dfe4e8 0%,#c9cbbf 45%,#8a8a6a 70%,#4d6a32 100%)}
.hero-after{left:600px;top:0;width:600px;height:400px;background:linear-gradient(180deg,#c7ced6 0%,#e9ecee 45%,#9aa39a 68%,#4f8a2f 100%)}
.hero-divider{left:594px;top:0;width:6px;height:400px;background:#fff}
.hero-shade{left:0;top:0;width:1200px;height:120px;background:linear-gradient(180deg,rgba(0,0,0,.35),rgba(0,0,0,0))}
.brand{left:143px;top:0;width:112px;height:117px;background:#fff;display:flex;flex-direction:column;align-items:center;justify-content:center;gap:6px}
.brand-dot{width:34px;height:34px;border-radius:50%;background:var(--green)}
.brand-name{font-family:"Montserrat",sans-serif;font-weight:700;font-size:11px;color:var(--green);text-align:center;line-height:1.2}
.nav{left:352px;top:52px;width:508px;display:flex;justify-content:space-between;white-space:nowrap;font-family:"Montserrat",sans-serif;font-weight:600;font-size:9.5px;color:#fff}
.btn-login,.btn-register{top:45px;height:26px;font-family:"Montserrat",sans-serif;font-weight:700;font-size:10.5px;color:#fff;display:flex;align-items:center;justify-content:center;border-radius:2px}
.btn-login{left:886px;width:74px;background:var(--blue)}
.btn-register{left:966px;width:89px;background:var(--green)}
/* property bar */
.prop-title{left:143px;top:400px;width:358px;height:64px;background:var(--black);color:#fff;padding:11px 18px}
.prop-title h1{font-family:"Montserrat",sans-serif;font-weight:500;font-size:16px;letter-spacing:.2px}
.prop-title p{font-size:11px;color:#ccc;margin-top:5px}
.prop-stats{left:501px;top:400px;width:320px;height:64px;display:flex;background:var(--green)}
.prop-stat{flex:1;display:flex;flex-direction:column;align-items:center;justify-content:center;gap:6px;color:#fff;font-size:11px;border-left:1px solid rgba(255,255,255,.35)}
.prop-stat:first-child{border-left:0}
/* main */
.video{left:143px;top:497px;width:678px;height:384px;background:linear-gradient(180deg,#4a86d4 0%,#b8d2ee 45%,#9a5a3c 62%,#6c8f4a 78%,#5a9a36 100%)}
.play{left:448px;top:658px;width:70px;height:70px}
.thumbs{left:143px;top:881px;width:678px;height:92px;background:var(--pale)}
.thumb{top:890px;width:103px;height:72px}
.t1{left:205px;background:linear-gradient(#6fa3de,#a66244 60%,#5f9a3a);outline:3px solid var(--green)}
.t2{left:318px;background:linear-gradient(#7aaee3,#b06a48 60%,#6a9a42)}
.t3{left:430px;background:linear-gradient(#5d98d8,#3a6ea0 55%,#8a9a7a)}
.t4{left:543px;background:linear-gradient(#8cb8e6,#e6e0d6 50%,#7a3a2a)}
.t5{left:656px;background:linear-gradient(#4f8a3a,#7aa65a 50%,#3f6a2a)}
.arrow-l,.arrow-r{top:914px}
.arrow-l{left:166px}.arrow-r{left:773px}
.section-h{font-family:"Montserrat",sans-serif;font-weight:500;font-size:15px;color:var(--ink);letter-spacing:.3px}
.about-h{left:143px;top:1004px}
.about-rule{left:143px;top:1034px;width:80px;height:2px;background:var(--green)}
.about-p{left:143px;top:1053px;width:668px;font-size:11px;line-height:18.5px;color:#333}
/* profit table */
.calc{left:143px;top:1187px;width:678px;height:240px;border:2px solid var(--line);padding:0 24px}
.calc-row{display:flex;justify-content:space-between;align-items:center;height:47.5px;border-bottom:2px solid var(--line);font-size:14px;color:#333}
.calc-row .val{font-weight:600;color:#111;display:flex;gap:14px}
.calc-row .minus{width:8px;font-weight:700}
.calc-row.total{border-bottom:0;font-family:"Montserrat",sans-serif;font-weight:700;color:#111;padding-left:4px}
.calc-row.total .val{color:var(--blue);padding-right:22px}
/* tabs */
.tab-info{left:143px;top:1464px;width:164px;height:38px;background:#fff;border:1px solid var(--line);border-bottom:0;display:flex;align-items:center;padding-left:32px;font-size:12px;color:#222}
.tab-feat{left:307px;top:1464px;width:164px;height:38px;background:var(--green);display:flex;align-items:center;justify-content:center;font-size:12px;color:#fff}
.tab-panel{left:143px;top:1501px;width:678px;height:161px;border:2px solid var(--line);padding:26px 30px}
.spec-grid{display:grid;grid-template-columns:200px 235px 200px;row-gap:15px;font-size:11.5px;color:#333}
.spec{display:flex;white-space:nowrap}
.spec b{font-weight:400;width:90px}
.spec .k2{width:60px}
/* share */
.share{left:143px;top:1697px;display:flex;align-items:center;gap:22px;font-size:12.5px;color:#333}
.share-sep{width:1px;height:32px;background:var(--line)}
.soc{width:34px;height:34px;display:flex;align-items:center;justify-content:center}
.soc.active{background:var(--blue-dark)}
/* contact agent */
.contact-h{left:143px;top:1764px;font-family:"Montserrat",sans-serif;font-size:12.5px;font-weight:500;color:#222}
.field{left:143px;width:272px;border:1px solid #cfcfcf;font-size:10px;color:#888;padding:0 12px;display:flex;align-items:center}
.f1{top:1801px;height:32px}.f2{top:1840px;height:32px}
.f3{top:1879px;height:65px;align-items:flex-start;padding-top:10px}
.submit{left:143px;top:1956px;width:80px;height:30px;background:var(--blue-dark);color:#fff;font-family:"Montserrat",sans-serif;font-weight:700;font-size:11px;display:flex;align-items:center;justify-content:center}
.agent-photo{left:456px;top:1772px;width:183px;height:179px;background:linear-gradient(180deg,#f1f2f4 0%,#e4e6ea 55%,#2b2f38 100%)}
.agent{left:659px;top:1771px}
.agent h3{font-family:"Montserrat",sans-serif;font-weight:600;font-size:12px;color:#222;margin-bottom:16px}
.agent li{list-style:none;display:flex;align-items:center;gap:12px;font-size:11px;color:#333;margin:0 0 9px 2px}
/* sidebar */
.search-box{left:845px;top:434px;width:210px;height:417px;border:1px solid #e3e3e3}
.side-h{font-family:"Montserrat",sans-serif;font-weight:500;font-size:15px;color:#222;text-align:center}
.side-rule{width:80px;height:2px;background:var(--green);margin:10px auto 0}
.search-box .side-h{margin-top:24px}
.s-field{position:absolute;left:19px;width:169px;height:32px;border:1px solid #d6d6d6;font-size:9.5px;color:#999;display:flex;align-items:center;justify-content:space-between;padding:0 12px}
.s-btn{position:absolute;left:19px;top:360px;width:169px;height:32px;background:var(--blue-dark);color:#fff;font-family:"Montserrat",sans-serif;font-weight:600;font-size:10.5px;display:flex;align-items:center;justify-content:center;gap:8px}
.cat-box{left:845px;top:873px;width:210px;height:209px;border:1px solid #e3e3e3}
.cat-box .side-h{margin-top:26px}
.cat-list{margin:20px 0 0 25px;list-style:none}
.cat-list li{display:flex;align-items:center;gap:10px;font-size:10.5px;color:#333;height:28px}
.cat-list li.on{color:var(--green)}
/* CTA band */
.cta{left:0;top:2046px;width:1200px;height:159px;background:var(--band)}
.cta h2{position:absolute;left:179px;top:52px;font-family:"Montserrat",sans-serif;font-weight:500;font-size:22px;color:#111;letter-spacing:.3px}
.cta p{position:absolute;left:179px;top:83px;font-size:12px;color:#333}
.cta-phone{position:absolute;left:826px;top:53px;width:197px;height:40px;background:var(--blue-dark);color:#fff;font-family:"Montserrat",sans-serif;font-size:19px;display:flex;align-items:center;justify-content:center}
/* footer */
.f-col{top:2255px;width:220px}
.f-col h4{font-family:"Montserrat",sans-serif;font-weight:600;font-size:11px;color:var(--green);margin-bottom:14px}
.f-col li{list-style:none;font-size:10px;color:#222;height:22.5px}
.f-col li.more{color:var(--green)}
.c1{left:145px}.c2{left:378px}.c3{left:613px}.c4{left:847px}
.f-rule{left:143px;top:2442px;width:912px;height:1px;background:#e3e3e3}
.copy{left:145px;top:2462px;font-size:10px;color:#333}
.f-soc{top:2457px;width:25px;height:25px;border-radius:50%;background:var(--blue);display:flex;align-items:center;justify-content:center}
</style>
</head>
<body>

<div class="abs hero-before" role="img" aria-label="Photo of a weathered two-storey house before renovation"></div>
<div class="abs hero-after" role="img" aria-label="Photo of the same house freshly renovated in white with a green lawn"></div>
<div class="abs hero-divider"></div>
<div class="abs hero-shade"></div>

<div class="abs brand"><span class="brand-dot"></span><span class="brand-name">VELMORA<br>PROPERTY SOLUTIONS</span></div>
<nav class="abs nav"><span>HOME</span><span>BUY</span><span>ABOUT US</span><span>INVESTOR INQUIRIES</span><span>HOW IT WORKS</span><span>CASE STUDIES</span></nav>
<div class="abs btn-login">LOGIN</div>
<div class="abs btn-register">REGISTER</div>

<div class="abs prop-title"><h1>45 - Villa Precy Subdivision Street, FL</h1><p>Bosnia Park, San Francisco, United States</p></div>
<div class="abs prop-stats">
  <div class="prop-stat"><svg width="13" height="13" viewBox="0 0 14 14"><circle cx="7" cy="7" r="7" fill="#fff"/><text x="7" y="10.5" font-size="10" text-anchor="middle" fill="#3aa335" font-family="Arial">$</text></svg>$ 700,000</div>
  <div class="prop-stat"><svg width="16" height="11" viewBox="0 0 16 11"><rect x="0" y="0" width="2" height="11" fill="#fff"/><rect x="0" y="5" width="16" height="3" fill="#fff"/><rect x="14" y="5" width="2" height="6" fill="#fff"/><rect x="3" y="2" width="4" height="3" fill="#fff"/></svg>3 Bed rooms</div>
  <div class="prop-stat"><svg width="13" height="13" viewBox="0 0 14 14"><circle cx="7" cy="7" r="7" fill="#fff"/><rect x="3" y="6" width="8" height="3" fill="#3aa335"/></svg>3 Bath rooms</div>
</div>

<div class="abs video" role="img" aria-label="Video still of red-brick new-build homes under a blue sky"></div>
<svg class="abs play" viewBox="0 0 70 70"><circle cx="35" cy="35" r="32" fill="none" stroke="#1a6fc9" stroke-width="4"/><circle cx="35" cy="35" r="28" fill="rgba(255,255,255,.2)"/><path d="M28 22 L50 35 L28 48 Z" fill="#1a6fc9"/></svg>

<div class="abs thumbs"></div>
<svg class="abs arrow-l" width="22" height="22" viewBox="0 0 22 22"><circle cx="11" cy="11" r="10" fill="none" stroke="#999" stroke-width="1.5"/><path d="M13 6 L8 11 L13 16" fill="none" stroke="#999" stroke-width="1.5"/></svg>
<div class="abs thumb t1" role="img" aria-label="Thumbnail of brick homes"></div>
<div class="abs thumb t2" role="img" aria-label="Thumbnail of brick homes along a street"></div>
<div class="abs thumb t3" role="img" aria-label="Thumbnail of a modern building"></div>
<div class="abs thumb t4" role="img" aria-label="Thumbnail of a timber-framed house"></div>
<div class="abs thumb t5" role="img" aria-label="Thumbnail of a house among trees"></div>
<svg class="abs arrow-r" width="22" height="22" viewBox="0 0 22 22"><circle cx="11" cy="11" r="10" fill="none" stroke="#3aa335" stroke-width="1.5"/><path d="M9 6 L14 11 L9 16" fill="none" stroke="#3aa335" stroke-width="1.5"/></svg>

<h2 class="abs section-h about-h">ABOUT PROPERTIES</h2>
<div class="abs about-rule"></div>
<p class="abs about-p">Lorem ipsum dolor sit amet, consectetur adipiscing elit. Nunc sollicitudin nibh non lectus pretium scelerisque. Nam facilisis tortor sed dolor convallis, eget consequat erat sagittis. Cras eu faucibus enim. Integer a bibendum erat. Donec feugiat est euismod metus blandit dignissim. Quisque varius non ante a tincidunt. Sed lobortis imperdiet nulla in imperdiet. Morbi cursus sollicitudin quam, et vulputate augue ultricies eu. Morbi egestas sed elit quis auctor. Vivamus sagittis diam nec varius luctus. Nulla auctor rhoncus odio, quis porta est dictum et. Curabitur a varius ligula. Sed ac commodo risus, sed vulputate nisl. Vivamus rhoncus lectus porta nibh hendrerit volutpat.</p>

<div class="abs calc">
  <div class="calc-row"><span>amount the property was bought</span><span class="val">200,000<span class="minus"></span></span></div>
  <div class="calc-row"><span>what the investor got in return</span><span class="val">100,000<span class="minus">–</span></span></div>
  <div class="calc-row"><span>rehab costs</span><span class="val">10,000<span class="minus">–</span></span></div>
  <div class="calc-row"><span>taxes and fees</span><span class="val">11,000<span class="minus">–</span></span></div>
  <div class="calc-row total"><span>NET PROFIT</span><span class="val">7,800</span></div>
</div>

<div class="abs tab-info">Information</div>
<div class="abs tab-feat">Features</div>
<div class="abs tab-panel">
  <div class="spec-grid">
    <div class="spec"><b>Price</b>:&nbsp;&nbsp;$800,000.00</div>
    <div class="spec"><b class="k2">Country</b>:&nbsp;&nbsp;United States</div>
    <div class="spec"><b>Garages</b>:&nbsp;&nbsp;1</div>
    <div class="spec"><b>For Sale/Rent</b>:&nbsp;&nbsp;Sale</div>
    <div class="spec"><b class="k2">Address</b>:&nbsp;&nbsp;Bosnia Park Apartment</div>
    <div class="spec"><b>Bedrooms</b>:&nbsp;&nbsp;3</div>
    <div class="spec"><b>Property Types</b>:&nbsp;&nbsp;Residential</div>
    <div class="spec"><b class="k2">City</b>:&nbsp;&nbsp;San Francisco</div>
    <div class="spec"><b>Bathrooms</b>:&nbsp;&nbsp;2</div>
    <div class="spec"><b>State</b>:&nbsp;&nbsp;OH</div>
    <div class="spec"><b class="k2">Area</b>:&nbsp;&nbsp;10,000 Sq.Ft</div>
    <div class="spec"><b>State</b>:&nbsp;&nbsp;OH</div>
  </div>
</div>

<div class="abs share">
  <span>Shared</span>
  <svg width="14" height="14" viewBox="0 0 14 14"><circle cx="11" cy="3" r="2" fill="#888"/><circle cx="3" cy="7" r="2" fill="#888"/><circle cx="11" cy="11" r="2" fill="#888"/><path d="M11 3 L3 7 L11 11" stroke="#888" fill="none"/></svg>
  <span class="share-sep"></span>
  <span class="soc active" aria-label="Share"><svg width="14" height="14" viewBox="0 0 14 14"><path d="M7 1 V9 M3.5 4.5 L7 1 L10.5 4.5" fill="none" stroke="#fff" stroke-width="1.6"/><path d="M2 8 V12.5 H12 V8" fill="none" stroke="#fff" stroke-width="1.6"/></svg></span>
  <span class="soc" aria-label="Comment"><svg width="14" height="13" viewBox="0 0 14 13"><path d="M1 1 H13 V9 H5 L2 12 V9 H1 Z" fill="none" stroke="#9a9a9a" stroke-width="1.3"/></svg></span>
  <span class="soc" aria-label="Copy link"><svg width="14" height="14" viewBox="0 0 14 14"><rect x="1" y="5" width="7" height="4" rx="2" fill="none" stroke="#9a9a9a" stroke-width="1.3"/><rect x="6" y="5" width="7" height="4" rx="2" fill="none" stroke="#9a9a9a" stroke-width="1.3"/></svg></span>
  <span class="soc" aria-label="Bookmark"><svg width="10" height="13" viewBox="0 0 10 13"><path d="M1 1 H9 V12 L5 9 L1 12 Z" fill="none" stroke="#9a9a9a" stroke-width="1.3"/></svg></span>
  <span class="soc" aria-label="Print"><svg width="14" height="13" viewBox="0 0 14 13"><rect x="3.5" y="1" width="7" height="3" fill="none" stroke="#9a9a9a" stroke-width="1.2"/><rect x="1" y="4" width="12" height="5" fill="none" stroke="#9a9a9a" stroke-width="1.2"/><rect x="3.5" y="8" width="7" height="4" fill="#fff" stroke="#9a9a9a" stroke-width="1.2"/></svg></span>
  <span class="soc" aria-label="Email"><svg width="14" height="10" viewBox="0 0 14 10"><rect x=".5" y=".5" width="13" height="9" fill="none" stroke="#999"/><path d="M.5 .5 L7 5.5 L13.5 .5" fill="none" stroke="#999"/></svg></span>
</div>

<h3 class="abs contact-h">CONTACT AGENT</h3>
<div class="abs field f1">Name</div>
<div class="abs field f2">E-mail</div>
<div class="abs field f3">Message</div>
<div class="abs submit">SUBMIT</div>

<div class="abs agent-photo" role="img" aria-label="Portrait photo of the listing agent"></div>
<div class="abs agent">
  <h3>Agent Marisa Kendal</h3>
  <ul>
    <li><svg width="10" height="10" viewBox="0 0 10 10"><path d="M2 0 L4 3 L3 4 Q4 6 6 7 L7 6 L10 8 L8 10 Q1 9 0 2 Z" fill="#333"/></svg>Tel no: 555-210-4471</li>
    <li><svg width="10" height="10" viewBox="0 0 10 10"><rect x="2.5" y="0" width="5" height="10" rx="1" fill="#333"/></svg>Mobile: +63-5550-184</li>
    <li><svg width="10" height="10" viewBox="0 0 10 10"><rect x="2" y="0" width="6" height="3" fill="#333"/><rect x="0" y="3" width="10" height="5" fill="#333"/><rect x="2" y="7" width="6" height="3" fill="#333"/></svg>Fax: 555-318-2290</li>
  </ul>
</div>

<aside class="abs search-box">
  <h3 class="side-h">ADVANCED SEARCH</h3>
  <div class="side-rule"></div>
  <div class="s-field" style="top:81px">Property Name</div>
  <div class="s-field" style="top:121px">Address</div>
  <div class="s-field" style="top:161px">Property Type<svg width="8" height="5" viewBox="0 0 8 5"><path d="M0 0 L4 4 L8 0" fill="none" stroke="#999"/></svg></div>
  <div class="s-field" style="top:201px">Bed Room<svg width="8" height="5" viewBox="0 0 8 5"><path d="M0 0 L4 4 L8 0" fill="none" stroke="#999"/></svg></div>
  <div class="s-field" style="top:241px">Bath Room<svg width="8" height="5" viewBox="0 0 8 5"><path d="M0 0 L4 4 L8 0" fill="none" stroke="#999"/></svg></div>
  <div class="s-field" style="top:281px">Minimum Price<svg width="8" height="5" viewBox="0 0 8 5"><path d="M0 0 L4 4 L8 0" fill="none" stroke="#999"/></svg></div>
  <div class="s-field" style="top:321px">Maximum Price<svg width="8" height="5" viewBox="0 0 8 5"><path d="M0 0 L4 4 L8 0" fill="none" stroke="#999"/></svg></div>
  <div class="s-btn"><svg width="11" height="11" viewBox="0 0 11 11"><circle cx="4.5" cy="4.5" r="3.5" fill="none" stroke="#fff" stroke-width="1.6"/><path d="M7 7 L10.5 10.5" stroke="#fff" stroke-width="1.8"/></svg>SEARCH</div>
</aside>

<aside class="abs cat-box">
  <h3 class="side-h">CATEGORIES</h3>
  <div class="side-rule"></div>
  <ul class="cat-list">
    <li><svg width="11" height="11" viewBox="0 0 11 11"><rect x=".5" y=".5" width="10" height="10" fill="none" stroke="#3aa335"/><path d="M2.5 5.5 L4.5 7.5 L8.5 3" fill="none" stroke="#3aa335" stroke-width="1.4"/></svg>Commercial Properties</li>
    <li class="on"><svg width="11" height="11" viewBox="0 0 11 11"><rect x=".5" y=".5" width="10" height="10" fill="none" stroke="#3aa335"/><path d="M2.5 5.5 L4.5 7.5 L8.5 3" fill="none" stroke="#3aa335" stroke-width="1.4"/></svg>Featured Properties</li>
    <li><svg width="11" height="11" viewBox="0 0 11 11"><rect x=".5" y=".5" width="10" height="10" fill="none" stroke="#3aa335"/><path d="M2.5 5.5 L4.5 7.5 L8.5 3" fill="none" stroke="#3aa335" stroke-width="1.4"/></svg>Residential Properties</li>
    <li><svg width="11" height="11" viewBox="0 0 11 11"><rect x=".5" y=".5" width="10" height="10" fill="none" stroke="#3aa335"/><path d="M2.5 5.5 L4.5 7.5 L8.5 3" fill="none" stroke="#3aa335" stroke-width="1.4"/></svg>Vacant Land</li>
  </ul>
</aside>

<section class="abs cta">
  <h2>CONTACT US FOR MORE INFORMATION</h2>
  <p>Aenean eu leo quam. Pellentesque ornare sem lacinia quam venenatis vestibulum.</p>
  <div class="cta-phone">555-0192-480</div>
</section>

<div class="abs f-col c1"><h4>Real Estate</h4><ul><li>Browse all homes</li><li>Albuquerque real estate</li><li>Atlanta real estate</li><li>Austin real estate</li><li>Baltimore real estate</li><li class="more">more</li></ul></div>
<div class="abs f-col c2"><h4>Rentals</h4><ul><li>Rental Buildings</li><li>Atlanta apartments for rent</li><li>Austin apartments for rent</li><li>Baltimore apartments for rent</li><li>Boston apartments for rent</li><li class="more">more</li></ul></div>
<div class="abs f-col c3"><h4>Properties Categories</h4><ul><li>Homes</li><li>Apartment</li><li>Office</li><li>Hotel</li><li>Condominium</li><li class="more">more</li></ul></div>
<div class="abs f-col c4"><h4>Browse Home</h4><ul><li>California</li><li>Texas</li><li>New York</li><li>Florida</li><li>Illinois</li><li class="more">more</li></ul></div>
<div class="abs f-rule"></div>
<p class="abs copy">All rights reserved 2018.</p>
<span class="abs f-soc" style="left:966px" aria-label="Comment"><svg width="12" height="11" viewBox="0 0 14 13"><path d="M1 1 H13 V9 H5 L2 12 V9 H1 Z" fill="#fff"/></svg></span>
<span class="abs f-soc" style="left:998px" aria-label="Share"><svg width="12" height="12" viewBox="0 0 14 14"><circle cx="11" cy="3" r="2" fill="#fff"/><circle cx="3" cy="7" r="2" fill="#fff"/><circle cx="11" cy="11" r="2" fill="#fff"/><path d="M11 3 L3 7 L11 11" stroke="#fff" fill="none" stroke-width="1.3"/></svg></span>
<span class="abs f-soc" style="left:1030px" aria-label="Email"><svg width="12" height="9" viewBox="0 0 14 10"><rect x=".5" y=".5" width="13" height="9" fill="none" stroke="#fff" stroke-width="1.3"/><path d="M.5 .5 L7 5.5 L13.5 .5" fill="none" stroke="#fff" stroke-width="1.3"/></svg></span>

</body>
</html>
```